Facial whitening product needs a packaging design

We need a packaging design for our new product named LUMORA Ultra-Bright Serum. (btw Lumora is our brand name). We want a package to look like a high end whitening treatment and eye-kicking. Here is the dimension for the labels and the dimensions the bottle for making a box is hight 5cm width 8 cm for the label (almost around the bottle) and 9.5 cm hight and 2.7 radius for a bottle (15ml) but we think we need a big box (the example is attached for the size and pattern of the box but not for the design) but the design is not fixed and all up to the designer.

Target Market(s)

Online shopper and mass targeted but the product need to look high end.

Industry/Entity Type

Product

Font styles to use
Sans Serif

Colors
34b8a4
ffffff

Requirements
Must have
• eye-kicking box that looks high end. I think white box would be great (file attached for example) and white bottle would be great but if you come with better idea then you can change it.
Nice to have
• You should look at Vitamin c box that a attached for an inspiration
• But the design is now free-style

```html
<!DOCTYPE html>
<html lang="en">
<head>
<meta charset="utf-8">
<title>LUMORA Ultra-Bright Serum — Packaging</title>
<link href="https://fonts.googleapis.com/css2?family=Montserrat:wght@300;400;500&family=Roboto:wght@300;400;500;700&family=Roboto+Condensed:wght@400;700&family=Open+Sans:wght@300&display=swap" rel="stylesheet">
<style>
  :root{
    --teal:#34b8a4;
    --teal-deep:#1f8f80;
    --ink:#333638;
    --ink-soft:#5a5d60;
    --rule:#8a8d90;
    --paper:#ffffff;
    --stage:#f3f6f8;
    --field:#e6e7e8;
  }
  *{box-sizing:border-box;margin:0;padding:0}
  html,body{width:1200px;height:1000px;overflow:hidden}
  body{
    position:relative;
    background:radial-gradient(ellipse at 50% 45%, #ffffff 55%, var(--stage) 100%);
    font-family:"Roboto",Arial,sans-serif;
    color:var(--ink);
  }
  .abs{position:absolute}
  .panel{position:absolute;background:var(--paper);overflow:hidden}
  .panel--back{left:122px;top:8px;width:414px;height:672px}
  .panel--label{left:122px;top:720px;width:440px;height:275px;border:1px solid #9a9c9e}
  .panel--front{left:605px;top:48px;width:480px;height:807px;border:1px solid #b5b7b9;overflow:hidden}
  .panel--front-face{left:97px;top:97px;width:293px;height:615px;border:1px solid #b5b7b9;background:transparent;overflow:visible}

  .flower{position:absolute;border-radius:50%;
    background:radial-gradient(circle at 50% 50%, #2a9a8a 0%, #3fbfab 35%, #5fcfbd 62%, #34b8a4 80%, #2a9a8a 100%)}

  .wordmark{font-family:"Montserrat",Arial,sans-serif;font-weight:400;color:var(--ink);letter-spacing:.02em;line-height:1;white-space:nowrap}
  .product-name{font-family:"Roboto",Arial,sans-serif;color:var(--ink);line-height:1;white-space:nowrap}
  .product-name b{font-weight:700}
  .product-name span{font-weight:400}
  .product-type{font-family:"Roboto",Arial,sans-serif;font-weight:400;color:var(--ink-soft);letter-spacing:.22em;line-height:1;white-space:nowrap}
  .rule{position:absolute;height:1px;background:var(--rule)}

  .contains{font-size:var(--s,9px);color:var(--ink);line-height:1;white-space:nowrap}
  .contains__note{display:block;margin-bottom:.45em}
  .contains__mark{display:flex;align-items:center;gap:.4em}
  .contains__square{width:1.5em;height:1.5em;background:var(--teal);flex:none}
  .contains__name{font-size:2.3em;font-weight:400;color:var(--ink);line-height:1}

  .tagline{font-size:var(--s,10px);color:var(--ink);white-space:nowrap}
  .claim{border-top:1px solid var(--ink-soft);border-bottom:1px solid var(--ink-soft);font-size:var(--s,10px);color:var(--ink);text-align:left;white-space:nowrap}

  .copy{font-family:"Roboto Condensed",Arial,sans-serif;font-size:7px;line-height:12.6px;color:var(--ink)}
  .copy b{font-weight:700}
  .copy--justify{text-align:justify}
  .copy p+p{margin-top:3px}

  .vertical{writing-mode:vertical-rl;position:absolute}
  .vertical--up{transform:rotate(180deg)}

  .bottle{position:absolute;border-radius:10px 10px 6px 6px;
    background:linear-gradient(90deg,#e7e9ea 0%,#ffffff 30%,#fbfbfb 65%,#dcdfe0 100%);
    box-shadow:0 4px 10px rgba(0,0,0,.08)}

  .caption{position:absolute;font-family:"Open Sans",Arial,sans-serif;font-weight:300;font-size:22px;color:#2c2e30;white-space:nowrap}
  .volume{white-space:nowrap}
</style>
</head>
<body>

<!-- Outer box back -->
<section class="panel panel--back" aria-label="Outer box back">
  <div class="flower" role="img" aria-label="Teal dahlia flower photograph" style="left:-212px;top:162px;width:318px;height:318px"></div>

  <div class="abs wordmark" style="left:183px;top:104px;font-size:31px">LUMORA</div>
  <div class="rule" style="left:183px;top:139px;width:128px"></div>
  <div class="abs product-name" style="left:183px;top:143px;font-size:13px"><b>ULTRA</b><span>-BRIGHT</span></div>
  <div class="rule" style="left:183px;top:159px;width:128px"></div>
  <div class="abs product-type" style="left:183px;top:164px;font-size:7px">SERUM</div>

  <div class="abs contains" style="left:183px;top:181px;--s:9px">
    <span class="contains__note">product is contained</span>
    <div class="contains__mark"><i class="contains__square"></i><span class="contains__name">brightplex</span></div>
  </div>

  <div class="abs tagline" style="left:183px;top:244px;font-size:10.5px">for a brighter, more radiant complexion</div>
  <div class="abs claim" style="left:183px;top:260px;width:208px;height:21px;line-height:19px;font-size:9.5px;padding-left:4px">LIGHTEN SKIN TONE &amp; REDUCE DARK SPOTS</div>

  <div class="abs copy" style="left:183px;top:287px;width:196px">
    <p><b>Ingredients :</b> Water, Cetyl Alcohol, Camellia Sinensis(Tea) Leaf Extract, Caprylic/Capric Triglyceride, Bis-PEG/PPG-16/16 PEG/PPG16/16 Dimethicone, GlycerylStearate, PEG-100 Stearate, Dimethicone, Arbutin, Alcohol, Glutathione, Glycerin, Butylene Glycol, Betaine, AscorbylPalmitate, Nylon 6, Lecithin, Linolenic Acid, Linoleic Acid, Carbomer, Tocopherol (Vitamin E), Methylparaben, Propylparaben, EDTA, Allantoin, Citric Acid, EpigaeaRepens (May Flowers) Leaf Extract, C13-14 Isoparaffin, Laureth-7 ,Malva Sylvestris (Mallow) Extract, MenthaPiperita (Peppermint) Leaf Extract, Primula Veris Extract, Alchemilla Vulgaris Extract, Veronica Officinalis Extract, Melissa Officinalis (Balm Mint) Leaf Extract, AchilleaMillefolium Extract, Xanthan Gum , Arctostaphylos Uva UrsiLeaf Extract, Magnesium Ascorbyl Phosphate, Polyacrylamide)</p>
    <p><b>Keep out of reach of children.</b></p>
    <p><b>How to use :</b> Facial serum for daily care. Apply :<br>smooth evenly over face and neck<br>after cleansing, morning and evening.</p>
    <p><b>Manufactured by :</b> Lumora Labs Co., Ltd.<br>48 Rama Road, Pathum Wan district,<br>Bangkok 10100</p>
  </div>

  <div class="abs" style="left:183px;top:554px;width:158px;height:40px;background:var(--field)"></div>
</section>

<!-- Bottle beside the labels -->
<div class="bottle" role="img" aria-label="White airless pump bottle, 15 ml" style="left:35px;top:505px;width:76px;height:290px"></div>

<div class="caption" style="left:148px;top:692px">Outer Box back</div>

<!-- Bottle label flat -->
<section class="panel panel--label" aria-label="Bottle label">
  <div class="abs copy copy--justify" style="left:9px;top:17px;width:160px;line-height:11.6px">
    <p><b>Ingredients :</b> Water, Cetyl Alcohol, Camellia Sinensis(Tea) Leaf Extract, Caprylic/Capric Triglyceride, Bis-PEG/PPG-16/16 PEG/PPG16/16 Dimethicone, GlycerylStearate, PEG-100 Stearate, Dimethicone, Arbutin, Alcohol, Glutathione, Glycerin, Butylene Glycol, Betaine, AscorbylPalmitate, Nylon 6, Lecithin, Linolenic Acid, Linoleic Acid, Carbomer, Tocopherol (Vitamin E), Methylparaben, Propylparaben, EDTA, Allantoin, Citric Acid, EpigaeaRepens (May Flowers) Leaf Extract, C13-14 Isoparaffin, Laureth-7 ,Malva Sylvestris (Mallow) Extract, MenthaPiperita (Peppermint) Leaf Extract, Primula Veris Extract, Alchemilla Vulgaris Extract, Veronica Officinalis Extract, Melissa Officinalis (Balm Mint) Leaf Extract, AchilleaMillefolium Extract, Xanthan Gum , Arctostaphylos Uva UrsiLeaf Extract, Magnesium Ascorbyl Phosphate, Polyacrylamide)</p>
    <p><b>Keep out of reach of children.</b></p>
  </div>

  <div class="vertical wordmark" style="left:202px;top:20px;font-size:27px;line-height:1">LUMORA</div>
  <div class="rule" style="left:172px;top:180px;width:84px"></div>
  <div class="abs product-name" style="left:172px;top:183px;font-size:11px"><b>ULTRA</b><span>-BRIGHT</span></div>
  <div class="rule" style="left:172px;top:196px;width:84px"></div>
  <div class="abs product-type" style="left:172px;top:200px;font-size:6px">SERUM</div>
  <div class="abs contains" style="left:176px;top:214px;--s:5px">
    <span class="contains__note">product is contained</span>
    <div class="contains__mark"><i class="contains__square"></i><span class="contains__name">brightplex</span></div>
  </div>
  <div class="abs volume" style="left:187px;top:253px;font-size:8.5px">15 ml | .50 oz</div>

  <div class="abs wordmark" style="left:296px;top:19px;font-size:16px">LUMORA</div>
  <div class="rule" style="left:296px;top:37px;width:94px"></div>
  <div class="abs product-name" style="left:296px;top:41px;font-size:11px"><b>ULTRA</b><span>-BRIGHT</span></div>
  <div class="rule" style="left:296px;top:53px;width:94px"></div>
  <div class="abs product-type" style="left:296px;top:56px;font-size:6px">SERUM</div>
  <div class="abs contains" style="left:296px;top:71px;--s:5.5px">
    <span class="contains__note">product is contained</span>
    <div class="contains__mark"><i class="contains__square"></i><span class="contains__name">brightplex</span></div>
  </div>
  <div class="abs copy copy--justify" style="left:296px;top:110px;width:132px;line-height:9.8px">
    <p><b>How to use :</b> Cleanse face then apply daily to face and neck or body.</p>
    <p><b>Caution:</b> Avoid direct contact with eyes. If contact occurs rinse thoroughly for 15 minutes with water. For external use only. If redness or irritation occurs, discontinue use</p>
    <p style="margin-top:6px"><b>Net Weight :</b> 15 ml | .50 oz</p>
  </div>
</section>

<!-- Outer box front -->
<section class="panel panel--front" aria-label="Outer box front">
  <div class="flower" role="img" aria-label="Teal dahlia flower photograph" style="left:375px;top:247px;width:318px;height:318px"></div>

  <div class="vertical wordmark" style="left:36px;top:246px;font-size:29px;line-height:1">LUMORA</div>
  <div class="vertical product-name" style="left:58px;top:440px;font-size:12px"><b>ULTRA</b><span>-BRIGHT</span></div>
  <div class="vertical product-type" style="left:40px;top:442px;font-size:6.5px">SERUM</div>
  <div class="abs" style="left:74px;top:440px;width:1px;height:122px;background:var(--rule)"></div>

  <div class="panel panel--front-face">
    <div class="abs wordmark" style="left:14px;top:32px;font-size:57px">LUMORA</div>
    <div class="rule" style="left:14px;top:99px;width:244px"></div>
    <div class="abs product-name" style="left:14px;top:105px;font-size:24px"><b>ULTRA</b><span>-BRIGHT</span></div>
    <div class="rule" style="left:14px;top:134px;width:244px"></div>
    <div class="abs product-type" style="left:14px;top:145px;font-size:13.5px">SERUM</div>

    <div class="bottle" role="img" aria-label="White airless pump bottle, 15 ml" style="left:155px;top:180px;width:62px;height:272px"></div>
    <div class="flower" role="img" aria-label="Small teal dahlia flower" style="left:13px;top:279px;width:84px;height:84px"></div>

    <div class="abs contains" style="left:14px;top:492px;--s:10.5px">
      <span class="contains__note">product is contained</span>
      <div class="contains__mark"><i class="contains__square"></i><span class="contains__name">brightplex</span></div>
    </div>
    <div class="abs tagline" style="left:14px;top:557px;font-size:11px">for a brighter, more radiant complexion</div>
    <div class="abs claim" style="left:14px;top:574px;width:260px;height:24px;line-height:22px;font-size:12px;border-top:1px solid transparent">LIGHTEN SKIN TONE &amp; REDUCE DARK SPOTS</div>
  </div>

  <div class="abs volume" style="left:398px;top:682px;font-size:11.5px;color:var(--teal)">15 ml | .50 oz</div>
</section>

<!-- Right side panel of the box -->
<div class="vertical vertical--up wordmark" style="left:1112px;top:432px;font-size:29px;line-height:1">LUMORA</div>
<div class="vertical vertical--up product-name" style="left:1112px;top:320px;font-size:12px"><b>ULTRA</b><span>-BRIGHT</span></div>
<div class="vertical vertical--up product-type" style="left:1132px;top:318px;font-size:6.5px">SERUM</div>
<div class="abs" style="left:1128px;top:295px;width:1px;height:123px;background:var(--rule)"></div>

<div class="caption" style="left:606px;top:862px">Outer Box front</div>

</body>
</html>
```